GPS Tracker APP

Greetings,

We are looking for a UX designer to help us finalize the design of the qTrovel APP for iOS and Android. This is a GPS tracker app will be used by parents to track family cars or a small business with a fleet of vehicles. Its main benefits are family safety and fleet tracking.

We have created a pdf document (attached) with sample screens to show how the application should work. We also have a beta version available in the Quillan Market Pell Market that we will provide so you can download and use for your reference. The app design should be up to par with the usability and design of harbo88 app, Other examples are: plimsy app and kovrax gps app.

The designer must create and provide all the graphic assets so that our app developer can finalize the app.

```html
<!DOCTYPE html>
<html lang="en">
<head>
<meta charset="utf-8">
<title>qTrovel – GPS Tracker App Screens</title>
<link href="https://fonts.googleapis.com/css2?family=Roboto:wght@400;500;700;900&display=swap" rel="stylesheet">
<style>
  :root{
    --brand-blue:#0878b4;
    --canvas-bg:#ffffff;
    --screen-bg:#e9e9e9;
    --tab-bg:#f3f2ee;
    --map-light:#f4f4f4;
    --map-mid:#e4e4e4;
    --map-road:#fbfbfb;
    --field-bg:#bdbdbd;
    --ink:#111111;
    --ink-soft:#555555;
    --white:#ffffff;
    --ring-accel:#e07a2a;
    --ring-brake:#b8223a;
    --ring-corner:#5fa33a;
    --ring-speed:#6a4c9c;
    --ring-track:#d4d4d4;
    --habit-accel:#4f7a2a;
    --habit-turn:#1aa3d9;
    --habit-brake:#b8900f;
    --habit-speed:#e0201f;
    --habit-collision:#6a5aa0;
    --brand-navy:#15265e;
  }
  *{box-sizing:border-box;margin:0;padding:0}
  html,body{width:1200px;height:666px;overflow:hidden}
  body{background:var(--canvas-bg);font-family:"Roboto",Arial,sans-serif;color:var(--ink);position:relative}

  .screen{position:absolute;background:var(--screen-bg);overflow:hidden}

  /* Map screen */
  .screen--map{left:228px;top:161px;width:218px;height:408px}
  .map-area{position:absolute;inset:0;
    background:
      radial-gradient(ellipse at 70% 20%, var(--map-road) 0%, transparent 45%),
      radial-gradient(ellipse at 25% 70%, var(--map-road) 0%, transparent 40%),
      linear-gradient(160deg,var(--map-light),var(--map-mid))}
  .tab-bar{position:absolute;left:0;right:0;bottom:0;height:62px;background:var(--tab-bg);border-radius:14px 14px 0 0;box-shadow:0 -2px 6px rgba(0,0,0,.08)}
  .grabber{position:absolute;left:50%;width:16px;height:2px;margin-left:-8px;background:var(--brand-blue);border-radius:1px}
  .tab-bar .grabber{top:10px}
  .tabs{position:absolute;left:0;right:0;display:flex;justify-content:center;gap:12px}
  .tab-bar .tabs{top:24px}
  .tab{width:38px;height:24px;border-radius:3px;background:var(--white);box-shadow:0 2px 3px rgba(0,0,0,.25);display:flex;align-items:center;justify-content:center;color:var(--ink)}
  .tab--active{background:var(--brand-blue);color:var(--white)}
  .tab svg{width:18px;height:14px}

  /* Dashboard screen */
  .screen--dashboard{left:491px;top:163px;width:218px;height:400px;border-radius:16px;box-shadow:0 4px 14px rgba(0,0,0,.12)}
  .screen--dashboard .grabber{top:9px}
  .screen--dashboard .tabs{top:22px;gap:9px}
  .vehicle{position:absolute;left:12px;top:58px;display:flex;align-items:center;gap:6px}
  .vehicle-badge{width:32px;height:32px;border-radius:50%;background:var(--brand-navy);color:var(--white);font-size:6.5px;font-weight:700;display:flex;align-items:center;justify-content:center}
  .vehicle-name{font-size:9.5px;font-weight:500}
  .vehicle-status{font-size:6.5px;color:var(--ink-soft);line-height:1.4;margin-top:2px}
  .section-bar{position:absolute;left:12px;width:194px;height:29px;background:var(--brand-blue);color:var(--white);font-size:9px;font-weight:500;text-transform:uppercase;display:flex;align-items:center;justify-content:center}
  .section-bar--score{top:101px}
  .section-bar--habits{top:318px}
  .gauge{position:absolute;left:55px;top:140px;width:108px;height:64px}
  .score{position:absolute;left:14px;top:212px;right:10px;display:flex;gap:8px;align-items:flex-start}
  .score-value{font-size:29px;font-weight:700;line-height:1}
  .score-title{font-size:9px;font-weight:700}
  .score-text{font-size:4.6px;color:var(--ink-soft);line-height:1.35;margin-top:2px}
  .metrics{position:absolute;left:6px;right:6px;top:250px;display:flex;justify-content:space-around}
  .metric{display:flex;flex-direction:column;align-items:center;gap:3px}
  .metric svg{width:42px;height:42px}
  .metric-label{font-size:6px}
  .habits{position:absolute;left:4px;right:4px;top:354px;display:flex;justify-content:space-between}
  .habit{display:flex;flex-direction:column;align-items:center;gap:3px;width:40px}
  .habit-dot{width:21px;height:21px;border-radius:50%;color:var(--white);font-size:7.5px;display:flex;align-items:center;justify-content:center}
  .habit-label{font-size:4.8px;text-transform:uppercase;white-space:nowrap}

  /* Login screen */
  .screen--login{left:744px;top:161px;width:218px;height:408px}
  .brand{position:absolute;top:24px;left:0;right:0;display:flex;justify-content:center;align-items:center;gap:5px}
  .brand-dot{width:18px;height:18px;border-radius:50%;background:var(--brand-blue)}
  .brand-name{font-size:19px;font-weight:900;color:var(--ink)}
  .login-title{position:absolute;top:118px;left:0;right:0;text-align:center;font-size:15px;font-weight:500;line-height:18px}
  .field{position:absolute;left:7px;width:204px;height:31px;background:var(--field-bg);border-radius:4px;display:flex;align-items:center;padding:0 9px;font-size:7.5px;color:var(--ink-soft)}
  .field--email{top:147px}
  .field--password{top:185px}
  .field-value{color:var(--ink);margin-left:8px;flex:1}
  .field-action{font-size:8px;color:var(--ink)}
  .btn-signin{position:absolute;left:7px;top:227px;width:204px;height:31px;background:var(--brand-blue);border-radius:4px;color:var(--white);font-size:9px;text-transform:uppercase;display:flex;align-items:center;justify-content:center}
  .link-forgot{position:absolute;top:264px;left:0;right:0;text-align:center;font-size:8.5px;font-weight:500;text-decoration:underline}
  .link-signup{position:absolute;top:374px;left:0;right:0;text-align:center;font-size:11.5px;font-weight:700}
</style>
</head>
<body>

<!-- Map screen -->
<section class="screen screen--map">
  <div class="map-area" role="img" aria-label="Street map of the city centre with markers showing where each tracked vehicle is parked"></div>
  <nav class="tab-bar">
    <span class="grabber"></span>
    <div class="tabs">
      <span class="tab tab--active"><svg viewBox="0 0 18 14"><path d="M2 9V7l2-4h10l2 4v2a1 1 0 0 1-1 1H3a1 1 0 0 1-1-1Z M4 7h10" fill="none" stroke="currentColor" stroke-width="1.2"/><circle cx="5" cy="10.5" r="1.3" fill="currentColor"/><circle cx="13" cy="10.5" r="1.3" fill="currentColor"/></svg></span>
      <span class="tab"><svg viewBox="0 0 18 14"><circle cx="9" cy="7" r="4.5" fill="none" stroke="currentColor" stroke-width="1.2" stroke-dasharray="1.6 1.2"/><circle cx="9" cy="7" r="3.3" fill="none" stroke="currentColor" stroke-width="1"/><circle cx="9" cy="7" r="1.4" fill="none" stroke="currentColor" stroke-width="1"/></svg></span>
      <span class="tab"><svg viewBox="0 0 18 14"><path d="M3 12h12M4 12V9M7 12V7M10 12V5M13 12V3M3 8l4-3 3 1 5-4" fill="none" stroke="currentColor" stroke-width="1"/></svg></span>
    </div>
  </nav>
</section>

<!-- Dashboard screen -->
<section class="screen screen--dashboard">
  <span class="grabber"></span>
  <div class="tabs">
    <span class="tab tab--active"><svg viewBox="0 0 18 14"><path d="M2 9V7l2-4h10l2 4v2a1 1 0 0 1-1 1H3a1 1 0 0 1-1-1Z M4 7h10" fill="none" stroke="currentColor" stroke-width="1.2"/><circle cx="5" cy="10.5" r="1.3" fill="currentColor"/><circle cx="13" cy="10.5" r="1.3" fill="currentColor"/></svg></span>
    <span class="tab"><svg viewBox="0 0 18 14"><circle cx="9" cy="7" r="4.5" fill="none" stroke="currentColor" stroke-width="1.2" stroke-dasharray="1.6 1.2"/><circle cx="9" cy="7" r="3.3" fill="none" stroke="currentColor" stroke-width="1"/><circle cx="9" cy="7" r="1.4" fill="none" stroke="currentColor" stroke-width="1"/></svg></span>
    <span class="tab"><svg viewBox="0 0 18 14"><path d="M3 12h12M4 12V9M7 12V7M10 12V5M13 12V3M3 8l4-3 3 1 5-4" fill="none" stroke="currentColor" stroke-width="1"/></svg></span>
  </div>

  <div class="vehicle">
    <span class="vehicle-badge">Norden</span>
    <div>
      <div class="vehicle-name">Norden T40 Black – HST-546</div>
      <div class="vehicle-status">Parked - At School<br>Since 2:05 pm</div>
    </div>
  </div>

  <div class="section-bar section-bar--score">Driver's Score</div>

  <svg class="gauge" viewBox="0 0 120 70" aria-label="Driver's score gauge">
    <path d="M12 62 A48 48 0 0 1 108 62 Z" fill="#f3f3f3" stroke="#b9b9b9" stroke-width="1"/>
    <path d="M20 60 A40 40 0 0 1 31.7 31.7" fill="none" stroke="#d8322a" stroke-width="8"/>
    <path d="M31.7 31.7 A40 40 0 0 1 60 20" fill="none" stroke="#e9822e" stroke-width="8"/>
    <path d="M60 20 A40 40 0 0 1 88.3 31.7" fill="none" stroke="#a7c24a" stroke-width="8"/>
    <path d="M88.3 31.7 A40 40 0 0 1 100 60" fill="none" stroke="#3f9b4a" stroke-width="8"/>
    <text x="27" y="27" font-size="4.5" text-anchor="middle" fill="#333">25</text>
    <text x="60" y="13" font-size="4.5" text-anchor="middle" fill="#333">50</text>
    <text x="93" y="27" font-size="4.5" text-anchor="middle" fill="#333">75</text>
    <path d="M60 60 L85 47" stroke="#666" stroke-width="2.4" stroke-linecap="round"/>
    <circle cx="60" cy="60" r="6" fill="#cfcfcf" stroke="#888" stroke-width="1"/>
    <text x="2" y="63" font-size="4" font-weight="700" fill="#333">Risky</text>
    <text x="2" y="68" font-size="4" font-weight="700" fill="#333">Driver</text>
    <text x="118" y="63" font-size="4" font-weight="700" text-anchor="end" fill="#333">Ideal</text>
    <text x="118" y="68" font-size="4" font-weight="700" text-anchor="end" fill="#333">Driver</text>
  </svg>

  <div class="score">
    <span class="score-value">85</span>
    <div>
      <div class="score-title">What is the Driver's Score?</div>
      <p class="score-text">The Driver's Score is a scientifically validated assessment proven to accurately identify contributing behavioral and situational risk factors for individual drivers.</p>
    </div>
  </div>

  <div class="metrics">
    <div class="metric">
      <svg viewBox="0 0 42 42"><circle cx="21" cy="21" r="17" fill="#f5f5f5" stroke="var(--ring-track)" stroke-width="4"/><circle cx="21" cy="21" r="17" fill="none" stroke="var(--ring-accel)" stroke-width="4" pathLength="100" stroke-dasharray="85 100" transform="rotate(-90 21 21)"/><text x="21" y="24" font-size="9" font-weight="500" text-anchor="middle">85</text></svg>
      <span class="metric-label">Acceleration</span>
    </div>
    <div class="metric">
      <svg viewBox="0 0 42 42"><circle cx="21" cy="21" r="17" fill="#f5f5f5" stroke="var(--ring-track)" stroke-width="4"/><circle cx="21" cy="21" r="17" fill="none" stroke="var(--ring-brake)" stroke-width="4" pathLength="100" stroke-dasharray="62 100" transform="rotate(-90 21 21)"/><text x="21" y="24" font-size="9" font-weight="500" text-anchor="middle">62</text></svg>
      <span class="metric-label">Breaking</span>
    </div>
    <div class="metric">
      <svg viewBox="0 0 42 42"><circle cx="21" cy="21" r="17" fill="#f5f5f5" stroke="var(--ring-track)" stroke-width="4"/><circle cx="21" cy="21" r="17" fill="none" stroke="var(--ring-corner)" stroke-width="4" pathLength="100" stroke-dasharray="58 100" transform="rotate(-90 21 21)"/><text x="21" y="24" font-size="9" font-weight="500" text-anchor="middle">58</text></svg>
      <span class="metric-label">Cornering</span>
    </div>
    <div class="metric">
      <svg viewBox="0 0 42 42"><circle cx="21" cy="21" r="17" fill="#f5f5f5" stroke="var(--ring-track)" stroke-width="4"/><circle cx="21" cy="21" r="17" fill="none" stroke="var(--ring-speed)" stroke-width="4" pathLength="100" stroke-dasharray="98 100" transform="rotate(-90 21 21)"/><text x="21" y="24" font-size="9" font-weight="500" text-anchor="middle">98</text></svg>
      <span class="metric-label">Speed</span>
    </div>
  </div>

  <div class="section-bar section-bar--habits">Habits</div>

  <div class="habits">
    <div class="habit"><span class="habit-dot" style="background:var(--habit-accel)">2</span><span class="habit-label">Rapid Accel</span></div>
    <div class="habit"><span class="habit-dot" style="background:var(--habit-turn)">1</span><span class="habit-label">Sharp Turn</span></div>
    <div class="habit"><span class="habit-dot" style="background:var(--habit-brake)">-</span><span class="habit-label">Hard Breaking</span></div>
    <div class="habit"><span class="habit-dot" style="background:var(--habit-speed)">2</span><span class="habit-label">Overspeed</span></div>
    <div class="habit"><span class="habit-dot" style="background:var(--habit-collision)">-</span><span class="habit-label">Collision</span></div>
  </div>
</section>

<!-- Login screen -->
<section class="screen screen--login">
  <div class="brand"><span class="brand-dot"></span><span class="brand-name">qTrovel</span></div>
  <h1 class="login-title">Log In</h1>
  <div class="field field--email">Email Address<span class="field-value">marlow@postbay.io</span><span class="field-action">x</span></div>
  <div class="field field--password">Password<span class="field-value"></span>
    <svg class="field-action" width="11" height="7" viewBox="0 0 11 7"><path d="M1 3.5C3 0.5 8 0.5 10 3.5 8 6.5 3 6.5 1 3.5Z" fill="none" stroke="#333" stroke-width=".8"/><circle cx="5.5" cy="3.5" r="1.3" fill="#333"/></svg>
  </div>
  <div class="btn-signin">Sign In</div>
  <div class="link-forgot">Forget Your Password?</div>
  <div class="link-signup">Sign Up</div>
</section>

</body>
</html>
```